Digital Billboard Design: Winter Sales Event

I own a boutique furniture store in Calgary, AB (maplecrestdecor.ca) and I am looking to advertise our winter sale event on a new curved digital billboard (specs attached including required file type).

I have this billboard rented for 52-weeks so I will be looking to change the design every 4-weeks (i.e. this is intended to be an ongoing project).

The objective of this first billboard is to raise awareness around our annual winter sales event. The store itself is only a few blocks from the billboard so those commuting into downtown are just a short drive from the store.

I am looking for a fresh, clean, contemporary look that will grab your attention as you drive into downtown Calgary without presenting to much info so as to be distracting (and overwhelming -- the billboard does not need to contain all info on my current marketing material). I should also note that the store caters to a higher-end, more sophisticated clientele so the graphics need to reflect the brand (i.e. we are not Brennick Furniture or Couch Depot!).

I have attached three files:

Billboard specs
Current marketing material advertising sale (and all relevant data)
An idea that is from an American furniture store that I think is interesting

Target Market(s)

Upper middle class, sophisticated client who appreciates the finer things in life.

Industry/Entity Type

Furniture Store

Font styles to use
Sans Serif

Requirements
Must have
• Company Logo
• Winter Sales Event - 20 to 60% off
• Address: 2743 8th Ave SW
Nice to have
• Image of furniture -- see our website www.maplecrestdecor.ca -- any photo from this site can be used
Should not have
• Too much text or visual distration

```html
<!DOCTYPE html>
<html lang="en">
<head>
<meta charset="utf-8">
<title>Maplecrest Decor – Winter Sales Event Billboard</title>
<link rel="stylesheet" href="https://fonts.googleapis.com/css2?family=Montserrat:wght@300;400;700&display=swap">
<style>
  :root {
    --page-bg: #ffffff;
    --frame: #333333;
    --board-bg: #ffffff;
    --ink: #2a2a2a;
    --flake: #efeff3;
    --sofa-top: #c9c9c7;
    --sofa-mid: #bdbdbb;
    --sofa-base: #a8a8a5;
  }
  * { margin: 0; padding: 0; box-sizing: border-box; }
  html, body {
    width: 1200px; height: 1000px; overflow: hidden;
    background: var(--page-bg);
    font-family: "Montserrat", sans-serif;
  }
  .page-frame {
    position: absolute; left: 33px; top: 35px;
    width: 1137px; height: 936px;
    border: 3px solid var(--frame);
  }
  .billboard {
    position: absolute; left: 109px; top: 273px;
    width: 984px; height: 458px;
    background: var(--board-bg);
    box-shadow: 0 1px 6px rgba(0,0,0,0.12);
    overflow: hidden;
    color: var(--ink);
    text-align: center;
  }
  .snowflake {
    position: absolute; border-radius: 50%;
    background: var(--flake);
  }
  .snowflake--top-left { left: 3px; top: -8px; width: 250px; height: 250px; }
  .snowflake--right { left: 771px; top: 37px; width: 210px; height: 210px; }
  .snowflake--bottom-left { left: 91px; top: 267px; width: 200px; height: 200px; }
  .snowflake--bottom-right { left: 691px; top: 302px; width: 190px; height: 190px; }
  .snowflake--center { left: 440px; top: 60px; width: 160px; height: 160px; }
  .brand-name {
    position: absolute; left: 0; right: 0; top: 37px;
    font-size: 38px; font-weight: 400; letter-spacing: 5px;
    line-height: 1;
  }
  .store-address {
    position: absolute; left: 0; right: 0; top: 82px;
    font-size: 35px; font-weight: 300; letter-spacing: 0.3px;
    line-height: 1;
  }
  .featured-sofa {
    position: absolute; left: 191px; top: 137px;
    width: 606px; height: 236px;
    border-radius: 8px 8px 4px 4px;
    background: linear-gradient(180deg, var(--sofa-top) 0%, var(--sofa-mid) 60%, var(--sofa-base) 100%);
  }
  .sale-headline {
    position: absolute; left: 0; right: 0; top: 389px;
    font-size: 38px; font-weight: 400; line-height: 1;
  }
  .sale-headline .light { font-weight: 300; }
  .sale-headline strong { font-weight: 700; }
</style>
</head>
<body>
  <div class="page-frame"></div>
  <section class="billboard">
    <div class="snowflake snowflake--top-left" role="img" aria-label="Large pale snowflake decoration"></div>
    <div class="snowflake snowflake--center" role="img" aria-label="Pale snowflake decoration"></div>
    <div class="snowflake snowflake--right" role="img" aria-label="Pale snowflake decoration"></div>
    <div class="snowflake snowflake--bottom-left" role="img" aria-label="Pale snowflake decoration"></div>
    <div class="snowflake snowflake--bottom-right" role="img" aria-label="Pale snowflake decoration"></div>

    <h1 class="brand-name">MAPLECREST DECOR</h1>
    <p class="store-address">2743 8TH AVE SW, CALGARY, AB</p>
    <div class="featured-sofa" role="img" aria-label="Photo of a light grey tufted mid-century sofa on dark tapered legs"></div>
    <p class="sale-headline">WINTER <span class="light">SALES</span> EVENT - <strong>GET 20-60% OFF</strong></p>
  </section>
</body>
</html>
```